Haverill’s

I would like a high class looking card with my logo and contact details (as per uploaded) Elegant, professional and highest quality feel

The following text included …..
“All commercial and residential painting work, large or small. Highest quality finishes and service.”

Industry/Entity Type

Painting

Contact Information for Business Card

Name, phone number, address, email address, company logo

Requirements
Must have
• Double sided

```html
<!DOCTYPE html>
<html lang="en">
<head>
<meta charset="utf-8">
<title>Haverill’s – Business Card</title>
<link rel="stylesheet" href="https://fonts.googleapis.com/css2?family=Cinzel:wght@500;700&family=EB+Garamond:wght@400&family=Lato:wght@400;700&display=swap">
<style>
  :root {
    --backdrop: #2a2a2c;
    --card: #1b1b1c;
    --gold: #c08a3e;
    --silver: #d9d9d9;
  }
  * { box-sizing: border-box; margin: 0; padding: 0; }
  html, body { width: 1200px; height: 800px; overflow: hidden; }
  body {
    background: var(--backdrop);
    display: flex;
    align-items: center;
    justify-content: center;
    gap: 40px;
  }
  .card {
    position: relative;
    width: 540px;
    height: 310px;
    background: var(--card);
    border-radius: 22px;
    box-shadow: 0 14px 34px rgba(0,0,0,.45);
  }

  /* brand mark */
  .brand {
    position: absolute;
    display: flex;
    align-items: center;
    gap: 14px;
    font-family: "Cinzel", serif;
    font-weight: 500;
    color: var(--gold);
    white-space: nowrap;
  }
  .brand-dot {
    border-radius: 50%;
    border: 2px solid currentColor;
  }
  .brand-rule {
    position: absolute;
    height: 1px;
    background: var(--gold);
    opacity: .8;
  }

  /* front */
  .front .brand { top: 38px; left: 50%; transform: translateX(-50%); font-size: 38px; }
  .front .brand-dot { width: 46px; height: 46px; }
  .front .brand-rule { top: 98px; left: 150px; width: 240px; }
  .divider {
    position: absolute;
    left: 28px; right: 28px; top: 205px;
    height: 1px;
    background: var(--gold);
  }
  .person {
    position: absolute;
    left: 30px; top: 140px;
    color: var(--gold);
  }
  .person-name {
    font-family: "Cinzel", serif;
    font-weight: 700;
    font-size: 26px;
    letter-spacing: .5px;
  }
  .person-role {
    font-family: "Lato", sans-serif;
    font-size: 15px;
    margin-top: 2px;
  }
  .address {
    position: absolute;
    right: 30px; top: 152px;
    text-align: right;
    font-family: "Lato", sans-serif;
    font-size: 14px;
    line-height: 1.45;
    color: var(--gold);
  }
  .contacts {
    position: absolute;
    left: 30px; top: 222px;
    list-style: none;
    font-family: "Lato", sans-serif;
    color: var(--gold);
  }
  .contacts li { display: flex; align-items: center; gap: 10px; margin-bottom: 6px; }
  .contact-phone { font-size: 18px; font-weight: 700; }
  .contact-email { font-size: 15px; }
  .icon { width: 14px; height: 14px; fill: var(--gold); flex: none; }

  /* back */
  .back .brand { top: 88px; left: 50%; transform: translateX(-50%); font-size: 50px; color: var(--silver); }
  .back .brand-dot { width: 64px; height: 64px; }
  .back .brand-rule { top: 168px; left: 110px; width: 320px; background: var(--silver); opacity: .35; }
  .tagline {
    position: absolute;
    left: 0; right: 0; bottom: 46px;
    text-align: center;
    font-family: "EB Garamond", serif;
    font-size: 17px;
    line-height: 1.35;
    color: var(--gold);
  }
</style>
</head>
<body>

  <section class="card front" aria-label="Business card front">
    <div class="brand">
      <span class="brand-name">Haverill’s</span>
      <span class="brand-dot"></span>
    </div>
    <div class="brand-rule"></div>

    <div class="person">
      <p class="person-name">DANIEL HAVERILL</p>
      <p class="person-role">Owner</p>
    </div>

    <address class="address">
      42 Kowhai Lane<br>
      Tirau, 3410
    </address>

    <div class="divider"></div>

    <ul class="contacts">
      <li class="contact-phone">
        <svg class="icon" viewBox="0 0 24 24" aria-hidden="true"><path d="M6.6 10.8a15.1 15.1 0 0 0 6.6 6.6l2.2-2.2a1 1 0 0 1 1-.25 11.4 11.4 0 0 0 3.6.57 1 1 0 0 1 1 1V20a1 1 0 0 1-1 1A17 17 0 0 1 3 4a1 1 0 0 1 1-1h3.5a1 1 0 0 1 1 1c0 1.25.2 2.45.57 3.57a1 1 0 0 1-.25 1z"/></svg>
        021 555 0147
      </li>
      <li class="contact-email">
        <svg class="icon" viewBox="0 0 24 24" aria-hidden="true"><path d="M2 5h20v14H2z M3.5 6.5 12 12.5l8.5-6z" fill-rule="evenodd"/></svg>
        dhaverill@mail.example
      </li>
    </ul>
  </section>

  <section class="card back" aria-label="Business card back">
    <div class="brand">
      <span class="brand-name">Haverill’s</span>
      <span class="brand-dot"></span>
    </div>
    <div class="brand-rule"></div>

    <p class="tagline">
      All commercial and residential painting work,<br>
      large or small. Highest quality finishes and service.
    </p>
  </section>

</body>
</html>
```